Continuing Professional Development Seminars
Power Point Template
• 11 juin 2011 15:52 rubenqol
thanks Velmoro
• 9 juin 2011 11:07 Velmoro
congrats your first project :)
• 9 juin 2011 02:48 tkvolaris
rubenqol - can you please upload a new draft that has the following slides:
1 - The title slide from draft#15 (I think this might be exactly the same in all subsequent drafts)
2 - The content slide from draft#15
3 - The content slide from draft#66
4 - The content slide from draft#68
5 - The last slide from draft#69
6 - The last slide from draft#15
I would like to see both of the end slides in the same draft.
Thanks.
• 7 juin 2011 08:20 tkvolaris
Thank you to all the designers who have submitted designs to date. The quality of the work is outstanding and is making the decision difficult.
I am still considering ALL the designs and will probably make a final decision soon. However, the designs that seem to stand out at the moment include (in no particular order) draft#50/draft#72, draft#15 (and the variations), draft#62 and draft#54.
• 6 juin 2011 06:31 tkvolaris
Draft#15 – can you please make the following changes:
1. Replace the last slide with a variant of the first slide. This new slide should be the same as the first slide, but with the following changes:
• The colours of the main background graphic should be reversed – so that becomes a red graphic with a blue stipe (instead of a blue graphic with a red stripe).
• Change the text - “Welcome to our Presentation” to “Thank you”.
• Change the white text (location and date) to the contact details you currently have on the last slide.
2. Can we try three small variations to the header on the content slides? Firstly, can you make the line under the presentation header about an inch smaller (so that it doesn’t go all the way to the logo). Secondly, can you please do a variant that reverses the logo and the header title (so that the logo is on the right and the presentation title is on the left). Thirdly, can you try a variant that doesn’t have the presentation header at all – only the logo? I would prefer having a look at all three slides to see how it looks. Thanks.
• 2 juin 2011 06:02 tkvolaris
Some of the recent designs have been very good. I particularly like the very bold graphical styles on the front pages whilst I prefer the more minimalist approach to the content slides.
I know that I said previously to try using our logo as a background watermark. However, on second thoughts I don’t think it really works. The watermarks are OK on the first slides, but on the content slides it is very distracting.
So far, my favourite designs are draft#15 and drafts#25-26. However, many of the designs have things I like or don’t like. Specifically,
• Draft#25 and Draft #26 – These designs are very effective. A bold front page and simple content pages. I think we would need to lose the watermarks on the content pages, but otherwise, these designs are on the right track.
• Draft#23 – I like the footer design of each content slide. Very simple and elegant.
• Draft#15 – perhaps my favourite design so far. Good bold first slide. The content slides are also good – maybe a little too busy as the moment?
• Draft#9 and Draft#10 – The first slides in these designs are very good. I like the strong bold designs. The content pages don’t really work – too much graphical background and not enough white space for content. One thing I like about these designs is the reverse colours of the background on the final slides.
Some of the other designs have similar good and bad points. However, I think I would be repeating myself if I discussed each one.
In summary, I like the first slides that are bold and emphasise our brand. The content slides should be simple, elegant and consistent.
• 31 mai 2011 19:56 tkvolaris
When I was looking through other projects on this website, there is one that I found that seems to be very effective. The project name is "Brisk Lanterns PowerPoint Template" and the design is draft#39.
I am not suggesting that I want a copy or a redraft of this design. It is just an example of something that I like.
• 31 mai 2011 19:47 tkvolaris
I like the designs that are creatively using the "swirls" on our logo. The first pages in draft#9 and draft#10 are interesting. I also didn't mind the first page in draft#11 (but note that it has been withdrawn?).
I think the logo needs to be more subtle on the content pages - maybe in the bottom right corner? Also maybe could use the logo as a watermark? Draft#4 uses a watermark, but being in the middle of the page, it might be a little distracting.

```html
<!DOCTYPE html>
<html lang="en">
<head>
<meta charset="utf-8">
<title>Norvane Seminar Slide Template</title>
<link href="https://fonts.googleapis.com/css2?family=Tinos:wght@400;700&family=Arimo:wght@400;700&display=swap" rel="stylesheet">
<style>
  :root {
    --page: #eceae6;
    --blue-deep: #0c1f7a;
    --blue: #1c3fae;
    --blue-bright: #2f5fd6;
    --red: #d4202a;
    --paper: #f7f7f5;
    --paper-edge: #d9d9d6;
    --muted: #7a7a7a;
    --white: #ffffff;
  }
  * { box-sizing: border-box; margin: 0; padding: 0; }
  html, body { width: 1200px; height: 922px; overflow: hidden; background: var(--page); }
  .canvas { position: relative; width: 1200px; height: 922px; }

  .slide {
    position: absolute; width: 520px; height: 380px; overflow: hidden;
    box-shadow: 0 4px 14px rgba(0,0,0,.25);
  }
  .slide--title { left: 70px; top: 70px; background: linear-gradient(180deg, var(--blue-bright) 0%, var(--blue) 40%, var(--blue-deep) 100%); }
  .slide--list  { left: 610px; top: 70px; }
  .slide--chart { left: 70px; top: 475px; }
  .slide--thanks { left: 610px; top: 475px; background: radial-gradient(ellipse at 50% 50%, var(--blue-bright) 0%, var(--blue) 45%, var(--blue-deep) 100%); }

  .brand-name {
    font-family: "Arimo", Arial, sans-serif; font-weight: 700; color: var(--blue);
    letter-spacing: 1px; line-height: 1; position: absolute; left: 50%; transform: translateX(-50%);
    white-space: nowrap;
  }

  /* title slide */
  .title-top { position: absolute; left: 0; top: 0; width: 520px; height: 100px; }
  .slide--title .brand-name { top: 20px; font-size: 26px; }
  .hero-photo {
    position: absolute; left: 0; top: 95px; width: 520px; height: 170px;
    background: linear-gradient(100deg, #c9d3df 0%, #eef1f4 45%, #9aa6b5 75%, #5b6678 100%);
  }
  .title-text { position: absolute; left: 58px; top: 284px; color: var(--white); font-family: "Tinos", "Times New Roman", serif; }
  .title-text h1 { font-size: 22px; font-weight: 700; letter-spacing: .5px; }
  .title-text p { font-size: 17px; margin-top: 2px; }

  /* content frame */
  .frame { position: absolute; inset: 0; background: linear-gradient(180deg, var(--paper) 0%, var(--paper-edge) 100%); }
  .frame svg { position: absolute; left: 0; width: 520px; }
  .frame .band-top { top: 0; height: 40px; }
  .frame .band-bottom { bottom: 0; height: 46px; }
  .frame .brand-name { font-size: 11px; }
  .frame .brand-name--top { top: 4px; color: var(--blue); }
  .frame .brand-name--bottom { bottom: 8px; color: var(--white); font-size: 13px; }

  .content-head { position: absolute; left: 28px; top: 46px; font-family: "Tinos", "Times New Roman", serif; }
  .content-head h2 { font-size: 17px; font-weight: 700; color: var(--blue); }
  .content-head p { font-size: 8px; font-weight: 700; color: var(--red); letter-spacing: .3px; }

  .group { font-family: "Arimo", Arial, sans-serif; width: 200px; }
  .group h3 { font-size: 8.5px; font-weight: 700; color: var(--blue); margin-bottom: 2px; }
  .group p { font-size: 6px; line-height: 1.35; color: var(--muted); }

  .list-grid {
    position: absolute; left: 28px; top: 92px; width: 470px;
    display: grid; grid-template-columns: 1fr 1fr; column-gap: 50px; row-gap: 22px;
  }
  .chart { position: absolute; left: 28px; top: 92px; width: 235px; height: 230px; }
  .chart-notes { position: absolute; left: 290px; top: 108px; display: flex; flex-direction: column; gap: 22px; }

  /* thanks slide */
  .thanks-mark {
    position: absolute; left: 50%; top: 50%; transform: translate(-50%, -50%);
    font-family: "Arimo", Arial, sans-serif; font-weight: 700; font-size: 96px; line-height: 1;
    color: rgba(255,255,255,.08); letter-spacing: 2px; white-space: nowrap;
  }
  .thanks-text {
    position: absolute; left: 0; right: 0; top: 150px; text-align: center;
    font-family: "Arimo", Arial, sans-serif; font-weight: 700; font-size: 29px; line-height: 1.2; color: var(--white);
    text-shadow: 0 2px 3px rgba(0,0,0,.35);
  }
</style>
</head>
<body>
<main class="canvas">

  <section class="slide slide--title">
    <svg class="title-top" viewBox="0 0 520 100" aria-hidden="true">
      <path d="M150,0 C170,80 350,80 370,0 Z" fill="#ffffff"/>
      <path d="M0,90 Q260,70 520,92" stroke="#d4202a" stroke-width="3" fill="none"/>
    </svg>
    <span class="brand-name">Norvane</span>
    <div class="hero-photo" role="img" aria-label="Photo of a business team meeting around a conference table"></div>
    <div class="title-text">
      <h1>TITLE OF PRESENTATION</h1>
      <p>Discription</p>
    </div>
  </section>

  <section class="slide slide--list">
    <div class="frame">
      <svg class="band-top" viewBox="0 0 520 40" preserveAspectRatio="none" aria-hidden="true">
        <path d="M0,0 H520 V36 Q260,12 0,36 Z" fill="#1c3fae"/>
        <path d="M0,36 Q260,12 520,36" stroke="#d4202a" stroke-width="2" fill="none"/>
        <path d="M210,0 C218,27 302,27 310,0 Z" fill="#ffffff"/>
      </svg>
      <span class="brand-name brand-name--top">Norvane</span>
      <svg class="band-bottom" viewBox="0 0 520 46" preserveAspectRatio="none" aria-hidden="true">
        <path d="M0,10 Q260,40 520,10" stroke="#d4202a" stroke-width="2" fill="none"/>
        <path d="M0,14 Q260,44 520,14 V46 H0 Z" fill="#1c3fae"/>
      </svg>
      <span class="brand-name brand-name--bottom">Norvane</span>
    </div>
    <header class="content-head">
      <h2>SAMPLE OF CONTENT LIST</h2>
      <p>DESCRIPTION IN THIS LINE</p>
    </header>
    <div class="list-grid">
      <div class="group"><h3>Group 01</h3><p>Short notes on this topic go here, with key points kept brief and clear for the audience to follow along.</p></div>
      <div class="group"><h3>Group 05</h3><p>Short notes on this topic go here, with key points kept brief and clear for the audience to follow along.</p></div>
      <div class="group"><h3>Group 02</h3><p>Short notes on this topic go here, with key points kept brief and clear for the audience to follow along.</p></div>
      <div class="group"><h3>Group 06</h3><p>Short notes on this topic go here, with key points kept brief and clear for the audience to follow along.</p></div>
      <div class="group"><h3>Group 03</h3><p>Short notes on this topic go here, with key points kept brief and clear for the audience to follow along.</p></div>
      <div class="group"><h3>Group 07</h3><p>Short notes on this topic go here, with key points kept brief and clear for the audience to follow along.</p></div>
      <div class="group"><h3>Group 04</h3><p>Short notes on this topic go here, with key points kept brief and clear for the audience to follow along.</p></div>
      <div class="group"><h3>Group 08</h3><p>Short notes on this topic go here, with key points kept brief and clear for the audience to follow along.</p></div>
    </div>
  </section>

  <section class="slide slide--chart">
    <div class="frame">
      <svg class="band-top" viewBox="0 0 520 40" preserveAspectRatio="none" aria-hidden="true">
        <path d="M0,0 H520 V36 Q260,12 0,36 Z" fill="#1c3fae"/>
        <path d="M0,36 Q260,12 520,36" stroke="#d4202a" stroke-width="2" fill="none"/>
        <path d="M210,0 C218,27 302,27 310,0 Z" fill="#ffffff"/>
      </svg>
      <span class="brand-name brand-name--top">Norvane</span>
      <svg class="band-bottom" viewBox="0 0 520 46" preserveAspectRatio="none" aria-hidden="true">
        <path d="M0,10 Q260,40 520,10" stroke="#d4202a" stroke-width="2" fill="none"/>
        <path d="M0,14 Q260,44 520,14 V46 H0 Z" fill="#1c3fae"/>
      </svg>
      <span class="brand-name brand-name--bottom">Norvane</span>
    </div>
    <header class="content-head">
      <h2>SAMPLE OF CONTENT LIST</h2>
      <p>DESCRIPTION IN THIS LINE</p>
    </header>
    <svg class="chart" viewBox="0 0 235 230" role="img" aria-label="Bar chart with six bars">
      <g stroke="#9a9a9a" stroke-width="0.8">
        <line x1="20" y1="20" x2="225" y2="20"/><line x1="20" y1="50" x2="225" y2="50"/>
        <line x1="20" y1="80" x2="225" y2="80"/><line x1="20" y1="110" x2="225" y2="110"/>
        <line x1="20" y1="140" x2="225" y2="140"/><line x1="20" y1="170" x2="225" y2="170"/>
        <line x1="20" y1="200" x2="225" y2="200" stroke="#555"/>
        <line x1="20" y1="20" x2="20" y2="200" stroke="#555"/>
      </g>
      <rect x="32" y="140" width="16" height="60" fill="#1c3fae"/>
      <rect x="64" y="52" width="16" height="148" fill="#1c3fae"/>
      <rect x="96" y="80" width="16" height="120" fill="#1c3fae"/>
      <rect x="128" y="128" width="16" height="72" fill="#d4202a"/>
      <rect x="160" y="108" width="16" height="92" fill="#d4202a"/>
      <rect x="192" y="150" width="16" height="50" fill="#1c3fae"/>
      <g font-family="Arimo, Arial, sans-serif" font-size="6" fill="#555" text-anchor="middle">
        <text x="40" y="210">Item 1</text><text x="72" y="210">Item 2</text><text x="104" y="210">Item 3</text>
        <text x="136" y="210">Item 4</text><text x="168" y="210">Item 5</text><text x="200" y="210">Item 6</text>
      </g>
    </svg>
    <div class="chart-notes">
      <div class="group"><h3>Group 01</h3><p>Short notes on this topic go here, with key points kept brief and clear for the audience to follow along.</p></div>
      <div class="group"><h3>Group 02</h3><p>Short notes on this topic go here, with key points kept brief and clear for the audience to follow along.</p></div>
      <div class="group"><h3>Group 03</h3><p>Short notes on this topic go here, with key points kept brief and clear for the audience to follow along.</p></div>
    </div>
  </section>

  <section class="slide slide--thanks">
    <span class="thanks-mark" aria-hidden="true">Norvane</span>
    <p class="thanks-text">THANK YOU FOR YOU<br>ATTENTION</p>
  </section>

</main>
</body>
</html>
```